Harbor Lights (title of music CD cover)

Create a CD jacket (front and back). Front artwork will be used on CD itself.The CD is an EP (6 songs). They are all love songs (Ballads). Violin, cello, piano, percussion, acoustic guitar, that sort of sound. I am looking for a sophisticated look to the CD. The title is Harbor Lights and the subtitle is The Song of Two. The picture is of me; Lia Brandt. I want this CD jacket to exude class. I have uploaded an example of what i think i want. Obviously rough on my part.

Besides the attached picture of me, I am looking for: my name, name of Cd (Harbor Lights) and subtitle (The Song of Two)
on front of CD

Back:
1. Every Star Grew Quiet (Lia Brandt) 3:26
2. Like Fresh Rain (Lia Brandt) 3:20
3. Once Again Near (Lia Brandt) 4:00
4. The Evening (Lia Brandt) 3:53
5. Here & Always (Lia Brandt) 3:27
6. Harbor Lights (Lia Brandt / Dean Morrow) 4:28
Producer: Dean Morrow
© 2017 Blue Meadow Ventures, LLC

I have some more to go on back: barcode, publishing, additional credits
Updates

Target Market(s)

Adults 25-55

Industry/Entity Type

Music Download

Colors

Designer to choose colors to be used in the design.

Requirements
Must have
• Pic of me on front with title, subtitle and my name

```html
<!DOCTYPE html>
<html lang="en">
<head>
<meta charset="utf-8">
<title>Harbor Lights — Lia Brandt</title>
<link rel="stylesheet" href="https://fonts.googleapis.com/css2?family=Poppins:wght@800&family=Open+Sans:wght@400&display=swap">
<style>
  :root {
    --bg-deep: #0b0b0b;
    --bg-mid: #262626;
    --wood-light: #d8b880;
    --wood-mid: #c29a5c;
    --wood-dark: #a47c42;
    --string: #bdbdbd;
    --subtitle: #8a8a8a;
    --portrait-warm: #8a7548;
    --portrait-shadow: #2a2418;
  }
  html, body { margin: 0; padding: 0; overflow: hidden; background: var(--bg-deep); }
  .cover { display: block; width: 1200px; height: 1200px; }
  .title-word { font-family: "Poppins", sans-serif; font-weight: 800; fill: url(#wood); }
  .artist-name { font-family: "Poppins", sans-serif; font-weight: 800; fill: url(#wood); }
  .subtitle { font-family: "Open Sans", sans-serif; font-weight: 400; fill: var(--subtitle); }
  .hanging-string { stroke: var(--string); stroke-width: 2; }
</style>
</head>
<body>
<svg class="cover" viewBox="0 0 1200 1200" xmlns="http://www.w3.org/2000/svg">
  <defs>
    <radialGradient id="backdrop" cx="0.6" cy="0.4" r="0.8">
      <stop offset="0" stop-color="var(--bg-mid)"/>
      <stop offset="1" stop-color="var(--bg-deep)"/>
    </radialGradient>
    <radialGradient id="portraitTone" cx="0.45" cy="0.45" r="0.6">
      <stop offset="0" stop-color="var(--portrait-warm)"/>
      <stop offset="0.6" stop-color="var(--portrait-shadow)"/>
      <stop offset="1" stop-color="var(--bg-deep)" stop-opacity="0"/>
    </radialGradient>
    <linearGradient id="wood" x1="0" y1="0" x2="1" y2="0.2">
      <stop offset="0" stop-color="var(--wood-mid)"/>
      <stop offset="0.35" stop-color="var(--wood-light)"/>
      <stop offset="0.7" stop-color="var(--wood-dark)"/>
      <stop offset="1" stop-color="var(--wood-light)"/>
    </linearGradient>
  </defs>

  <rect class="backdrop" width="1200" height="1200" fill="url(#backdrop)"/>

  <rect class="portrait" x="-120" y="200" width="800" height="1080" fill="url(#portraitTone)"
        role="img" aria-label="Warm sepia portrait photograph of the artist, Lia Brandt, head and shoulders, softly lit against the dark background"/>

  <g class="hanging">
    <line class="hanging-string" x1="704" y1="0" x2="704" y2="362"/>
    <line class="hanging-string" x1="1036" y1="0" x2="1036" y2="362"/>
  </g>

  <g class="title">
    <text class="title-word" x="568" y="470" font-size="132" textLength="600" lengthAdjust="spacingAndGlyphs">HARBOR</text>
    <text class="title-word" x="632" y="576" font-size="132" textLength="468" lengthAdjust="spacingAndGlyphs">LIGHTS</text>
  </g>

  <text class="subtitle" x="1148" y="684" font-size="52" text-anchor="end">The Song of Two</text>

  <text class="artist-name" x="1156" y="1146" font-size="80" text-anchor="end">LIA BRANDT</text>
</svg>
</body>
</html>
```